Business Card Design for Small Electrical Contractor

I need to update my business card into something a little more modern. We are a small electrical contracting company. We service domestic and commercial places around Sydney. We have 2 logo designs at the moment. I have uploaded both and 2 different sizes to work with.

Industry/Entity Type

Business

Contact Information for Business Card

Leo Hartigan
8/21-23 Birch Rd, Kelsworth 2087
t - (02) 9381 4720
m - 0427 815 903
E - info@hartiganelx.com.au
W - hartiganelx.com.au
ABN: 42 907 551 316

Font styles to use
Sans Serif

Requirements
Must have
• I would also like to see the below fit on somewhere aswell
• - Licensed Electrician
• - Level 2 (Cat 1 & 4)
• - Domestic
• - Commercial
• - Repairs and Installations
• - Data
Nice to have
• Try and keep similar colours as logo
Should not have
• No lightning bolts or light globes. Smart and professional please.

```html
<!DOCTYPE html>
<html lang="en">
<head>
<meta charset="utf-8">
<title>Hartigan Electrical – Business Card</title>
<link href="https://fonts.googleapis.com/css2?family=Raleway:wght@400;500;600;800&display=swap" rel="stylesheet">
<style>
  :root {
    --teal: #0b4a47;
    --teal-deep: #083836;
    --teal-light: #0f5e5a;
    --ink: #1f2a2a;
    --grey: #8a9090;
    --paper: #ffffff;
    --stage: #e9ecec;
  }
  * { box-sizing: border-box; margin: 0; padding: 0; }
  html, body { width: 1200px; height: 913px; overflow: hidden; }
  body {
    background: var(--stage);
    font-family: "Raleway", sans-serif;
    color: var(--ink);
    position: relative;
  }
  .card {
    position: absolute;
    width: 540px;
    height: 309px;
    background: var(--paper);
    box-shadow: 0 6px 18px rgba(0,0,0,.15);
    overflow: hidden;
  }
  .card-front { left: 40px; top: 130px; }
  .card-back { left: 620px; top: 474px; }

  /* front */
  .brand {
    position: absolute;
    left: 0; right: 0; top: 82px;
    display: flex;
    justify-content: center;
    align-items: center;
    gap: 10px;
  }
  .brand-mark {
    width: 14px; height: 14px;
    background: var(--teal);
  }
  .brand-name {
    font-weight: 600;
    font-size: 30px;
    color: var(--teal);
    letter-spacing: .5px;
  }
  .service-band { position: absolute; left: 0; top: 170px; width: 540px; height: 70px; }
  .service-text {
    position: absolute;
    left: 0; right: 0; top: 181px;
    text-align: center;
    color: var(--paper);
    font-size: 13.5px;
    line-height: 22px;
    letter-spacing: .3px;
  }

  /* back */
  .back-shapes { position: absolute; inset: 0; }
  .holder-name {
    position: absolute; left: 36px; top: 92px;
    font-size: 28px; font-weight: 400; color: var(--ink);
  }
  .holder-name strong { font-weight: 800; color: var(--teal); letter-spacing: .5px; }
  .abn {
    position: absolute; left: 38px; top: 132px;
    font-size: 12.5px; color: var(--grey); letter-spacing: .3px;
  }
  .address {
    position: absolute; left: 70px; top: 216px; width: 190px;
    text-align: center; font-size: 13px; line-height: 18px; color: var(--ink);
  }
  .address-icon { display: block; margin: 0 auto 6px; }
  .contact-list {
    position: absolute; left: 284px; top: 158px;
    list-style: none; color: var(--paper);
    font-size: 12.5px; letter-spacing: .3px;
  }
  .contact-list li { display: flex; align-items: center; gap: 9px; height: 20px; }
  .contact-icon { width: 14px; height: 14px; flex: none; }
</style>
</head>
<body>

<section class="card card-front" aria-label="Business card front">
  <div class="brand">
    <span class="brand-mark"></span>
    <span class="brand-name">Hartigan Electrical</span>
  </div>
  <svg class="service-band" viewBox="0 0 540 70" aria-hidden="true">
    <g stroke="var(--teal)" stroke-width="1.6" fill="none">
      <line x1="0" y1="27" x2="70" y2="27"/>
      <line x1="0" y1="33" x2="70" y2="33"/>
      <line x1="0" y1="39" x2="70" y2="39"/>
      <line x1="470" y1="27" x2="540" y2="27"/>
      <line x1="470" y1="33" x2="540" y2="33"/>
      <line x1="470" y1="39" x2="540" y2="39"/>
    </g>
    <polygon points="82,6 458,6 472,20 472,50 458,64 82,64 68,50 68,20" fill="var(--teal-deep)"/>
    <polygon points="86,10 454,10 467,23 467,47 454,60 86,60 73,47 73,23" fill="none" stroke="var(--paper)" stroke-width="1"/>
  </svg>
  <p class="service-text">Licensed Electrician | Level 2 (Cat 1 &amp; 4) | Domestic<br>Commercial | Repairs and Installations | Data</p>
</section>

<section class="card card-back" aria-label="Business card back">
  <svg class="back-shapes" viewBox="0 0 540 309" aria-hidden="true">
    <defs>
      <linearGradient id="tealFade" x1="0" y1="0" x2="0" y2="1">
        <stop offset="0" stop-color="var(--teal-light)"/>
        <stop offset="1" stop-color="var(--teal-deep)"/>
      </linearGradient>
    </defs>
    <rect x="300" y="0" width="240" height="160" fill="url(#tealFade)"/>
    <rect x="516" y="0" width="24" height="309" fill="var(--teal-deep)"/>
    <path d="M270 140 H540 V262 H288 Q270 262 270 244 V158 Q270 140 288 140 Z" fill="var(--teal-deep)"/>
    <path d="M372 128 H504 Q522 128 522 146 V232 Q522 250 504 250" fill="none" stroke="var(--paper)" stroke-width="2"/>
  </svg>

  <h1 class="holder-name">Leo <strong>HARTIGAN</strong></h1>
  <p class="abn">ABN: 42 907 551 316</p>

  <p class="address">
    <svg class="address-icon" width="18" height="18" viewBox="0 0 18 18" aria-hidden="true">
      <circle cx="9" cy="9" r="9" fill="var(--ink)"/>
      <path d="M4.5 9 L9 5 L13.5 9 M6 8.5 V13 H12 V8.5" fill="none" stroke="var(--paper)" stroke-width="1.4"/>
    </svg>
    8/21-23 Birch Rd<br>Kelsworth 2087
  </p>

  <ul class="contact-list">
    <li>
      <svg class="contact-icon" viewBox="0 0 14 14" aria-hidden="true"><circle cx="7" cy="7" r="7" fill="var(--paper)"/><path d="M4.5 4 Q4 8 9.5 10 L10.3 8.8 L8.8 7.9 L8 8.5 Q6.2 7.6 5.6 5.8 L6.2 5 L5.4 3.6 Z" fill="var(--teal-deep)"/></svg>
      (02) 9381 4720
    </li>
    <li>
      <svg class="contact-icon" viewBox="0 0 14 14" aria-hidden="true"><circle cx="7" cy="7" r="7" fill="var(--paper)"/><rect x="5" y="3.5" width="4" height="7" rx="0.8" fill="none" stroke="var(--teal-deep)" stroke-width="1.1"/></svg>
      0427 815 903
    </li>
    <li>
      <svg class="contact-icon" viewBox="0 0 14 14" aria-hidden="true"><circle cx="7" cy="7" r="7" fill="var(--paper)"/><circle cx="7" cy="7" r="3.6" fill="none" stroke="var(--teal-deep)" stroke-width="1"/><path d="M3.4 7 H10.6 M7 3.4 Q5 7 7 10.6 M7 3.4 Q9 7 7 10.6" fill="none" stroke="var(--teal-deep)" stroke-width="0.8"/></svg>
      hartiganelx.com.au
    </li>
    <li>
      <svg class="contact-icon" viewBox="0 0 14 14" aria-hidden="true"><circle cx="7" cy="7" r="7" fill="var(--paper)"/><rect x="3.8" y="4.8" width="6.4" height="4.6" fill="none" stroke="var(--teal-deep)" stroke-width="1"/><path d="M3.8 4.8 L7 7.4 L10.2 4.8" fill="none" stroke="var(--teal-deep)" stroke-width="1"/></svg>
      info@hartiganelx.com.au
    </li>
  </ul>
</section>

</body>
</html>
```